Business Card Design

I give lessons and clinics for dressage riders
I would like the design to be an outline (with broad lines) of a dressage horse and rider with in background of whole card with print over top tan or parchment card with burgundy print

Industry/Entity Type

Business

Contact Information for Business Card

Tod Harlick
555-317-0492
Classical dressage training for the modern American
Clinics, lessons, training level -Prix St. George

Requirements
Must have
• broad lined outline of dressage horse and rider

```html
<!DOCTYPE html>
<html lang="en">
<head>
<meta charset="utf-8">
<title>Tod Harlick — Classical Dressage</title>
<link href="https://fonts.googleapis.com/css2?family=Alegreya:ital,wght@0,400;1,400&family=Alegreya+SC:wght@400&display=swap" rel="stylesheet">
<style>
  :root {
    --parchment: #f1dfb4;
    --parchment-light: #f8ecc9;
    --parchment-dark: #e4c995;
    --burgundy: #8a1c3f;
    --cream: #f6e6bd;
  }
  html, body {
    margin: 0;
    padding: 0;
    overflow: hidden;
    background: #ffffff;
  }
  .card {
    position: relative;
    width: 686px;
    height: 1200px;
    overflow: hidden;
    background: radial-gradient(ellipse at 60% 30%, var(--parchment-light) 0%, var(--parchment) 55%, var(--parchment-dark) 100%);
  }
  .card-art {
    position: absolute;
    inset: 0;
    width: 686px;
    height: 1200px;
  }
  .card-text {
    position: absolute;
    left: 46px;
    top: 630px;
    right: 30px;
    color: var(--cream);
  }
  .name {
    margin: 0;
    font-family: "Alegreya SC", Georgia, serif;
    font-weight: 400;
    font-size: 68px;
    line-height: 1;
    letter-spacing: 0.02em;
  }
  .phone {
    margin: 30px 0 0;
    font-family: "Alegreya", Georgia, serif;
    font-weight: 400;
    font-size: 56px;
    line-height: 1;
    letter-spacing: 0.09em;
  }
  .tagline {
    margin: 26px 0 0;
    font-family: "Alegreya", Georgia, serif;
    font-style: italic;
    font-size: 44px;
    line-height: 72px;
  }
</style>
</head>
<body>
  <div class="card">
    <svg class="card-art" viewBox="0 0 686 1200" xmlns="http://www.w3.org/2000/svg">
      <defs>
        <radialGradient id="rider-tone" cx="50%" cy="45%" r="60%">
          <stop offset="0%" stop-color="#8a1c3f" stop-opacity="0.22"/>
          <stop offset="100%" stop-color="#8a1c3f" stop-opacity="0.04"/>
        </radialGradient>
      </defs>
      <rect class="illustration" x="12" y="0" width="662" height="420" rx="24"
            fill="url(#rider-tone)" role="img"
            aria-label="Broad-lined burgundy outline of a jumping horse with braided mane and a rider in a helmet, its tail sweeping into the curve below"/>
      <path class="wave-band"
            d="M0,594 C140,520 330,478 520,462 C600,455 650,440 686,395 L686,1200 L0,1200 Z"
            fill="var(--burgundy)"/>
    </svg>
    <div class="card-text">
      <h1 class="name">Tod Harlick</h1>
      <p class="phone">555-317-0492</p>
      <p class="tagline">Classical dressage training<br>for the modern American Clinics,<br>lessons, training level –<br>Prix St. George</p>
    </div>
  </div>
</body>
</html>
```